Birchway Swing Studio New Location Postcard

I need a postcard announcing our new location. It is a indoor golf training facility that offers award winner instruction, state-of-the-art technology, and custom club fitting. Whether you are a beginner, an aspiring athlete, or an amateur, Birchway Swing Studio offers personalized programs to help take your game to the next level. Call now to schedule your free tour or to sign up. Limited memberships available.
I would like somewhere are on postcard to say Don't put away your clubs just yet! The course may be closed but Birchway Swing Studio's new indoor location is open!
Industry/Entity Type
Training
Look and feel
Each slider illustrates characteristics of the customer's brand and the style your logo design should communicate.

```html
<!DOCTYPE html>
<html lang="en">
<head>
<meta charset="utf-8">
<title>Birchway Swing Studio – New Location Postcard</title>
<link href="https://fonts.googleapis.com/css2?family=Roboto+Condensed:ital,wght@0,400;0,700;0,900;1,700;1,900&display=swap" rel="stylesheet">
<style>
  :root {
    --red: #c8242a;
    --red-text: #d4302f;
    --navy: #1c2233;
    --ink: #111111;
    --olive: #cdd47a;
    --green-dark: #4f7d1a;
    --green-light: #a9c93c;
    --paper: #ffffff;
    --backdrop: #e8e9ea;
    --rule: #cfd3d8;
    --stamp: #f8e4dc;
  }
  * { box-sizing: border-box; margin: 0; padding: 0; }
  html, body { width: 1200px; height: 1200px; overflow: hidden; }
  body {
    background: var(--backdrop);
    font-family: "Roboto Condensed", "Arial Narrow", sans-serif;
    position: relative;
  }
  .postcard {
    position: absolute;
    left: 230px;
    width: 740px;
    height: 572px;
    overflow: hidden;
  }
  .postcard--back { top: 20px; background: var(--paper); }
  .postcard--front { top: 608px; background: var(--green-dark); }
  .abs { position: absolute; }

  /* Back side */
  .back__wash {
    left: 0; top: 150px; width: 560px; height: 360px;
    background: radial-gradient(ellipse at 30% 55%, rgba(190,215,240,.5), rgba(255,255,255,0) 70%);
  }
  .back__map {
    left: 250px; top: 0; width: 490px; height: 180px;
    background: linear-gradient(160deg, #f3f1ea 0%, #f7f6f2 60%, rgba(255,255,255,0) 100%);
  }
  .back__stamp { left: 571px; top: 33px; width: 134px; height: 134px; background: var(--stamp); }
  .brand { left: 36px; top: 48px; display: flex; align-items: center; gap: 12px; }
  .brand__dot { width: 52px; height: 52px; border: 3px solid var(--red); border-radius: 50%; flex: none; }
  .brand__name { font-size: 33px; font-weight: 700; font-style: italic; color: var(--red-text); line-height: 1; }
  .brand__tagline { font-size: 18px; font-weight: 700; font-style: italic; color: var(--ink); margin-top: 3px; }
  .offers { left: 44px; top: 128px; color: var(--ink); }
  .offers__title { font-size: 22px; font-weight: 700; line-height: 26px; margin-bottom: 2px; }
  .offers__list { list-style: none; font-size: 18.5px; line-height: 26px; }
  .offers__list li { position: relative; padding-left: 20px; }
  .offers__list li::before {
    content: ""; position: absolute; left: 0; top: 8px; width: 11px; height: 11px;
    border-radius: 50%; background: var(--red);
  }
  .intro { left: 44px; top: 240px; font-size: 14px; line-height: 17.5px; color: var(--ink); white-space: nowrap; }
  .golfer { left: 46px; top: 306px; width: 58px; height: 154px; background: linear-gradient(180deg, #3a3a3a, #111); }
  .cta { left: 108px; top: 307px; width: 226px; text-align: center; color: var(--red-text); font-weight: 700; line-height: 1; }
  .cta__line1 { font-size: 17px; }
  .cta__line2 { font-size: 20px; margin-top: 5px; }
  .contact { left: 144px; top: 366px; color: var(--navy); font-weight: 700; line-height: 1.1; }
  .contact__phone { font-size: 28px; }
  .contact__email { font-size: 20px; margin-top: 2px; }
  .footnote { left: 140px; top: 450px; font-size: 14px; color: #555; }
  .rule { left: 407px; width: 299px; border-top: 1.5px solid var(--rule); }

  /* Front side */
  .front__photo { left: 0; top: 0; width: 740px; height: 572px; }
  .front__band { left: 0; top: 0; width: 740px; height: 130px; }
  .headline {
    left: 0; top: 30px; width: 740px; text-align: center; line-height: 1;
    font-size: 41px; font-weight: 700; font-style: italic; color: var(--olive);
  }
  .front__map { left: 0; top: 0; width: 740px; height: 572px; }
  .pitch__lead { right: 36px; top: 150px; font-size: 27px; font-weight: 400; color: var(--ink); line-height: 1; }
  .pitch__name { right: 34px; top: 190px; font-size: 37px; font-weight: 900; color: var(--ink); line-height: 1; white-space: nowrap; }
  .pitch__tag {
    left: 336px; top: 246px; width: 196px; height: 30px; background: var(--paper);
    font-size: 25px; font-weight: 900; font-style: italic; color: var(--ink);
    line-height: 30px; text-align: right; padding-right: 6px;
  }
  .pitch__rest { left: 540px; top: 246px; font-size: 25px; font-weight: 700; font-style: italic; color: var(--ink); line-height: 30px; }
  .pitch__open { left: 408px; top: 276px; font-size: 104px; font-weight: 900; font-style: italic; color: var(--ink); line-height: 1; }
  .locator__card {
    left: 279px; top: 423px; width: 172px; height: 60px; background: var(--paper);
    padding: 3px 0 0 23px; font-size: 14px; font-weight: 700; line-height: 18px;
    color: var(--ink); font-style: normal;
  }
  .locator__dot {
    left: 238px; top: 425px; width: 54px; height: 54px; border-radius: 50%;
    background: var(--green-light); border: 4px solid var(--paper);
  }
</style>
</head>
<body>

<section class="postcard postcard--back" aria-label="Postcard back">
  <div class="abs back__wash" role="img" aria-label="Soft blue swoosh decoration"></div>
  <div class="abs back__map" role="img" aria-label="Faded street map around the studio"></div>
  <div class="abs back__stamp" aria-label="Stamp area"></div>

  <div class="abs brand">
    <span class="brand__dot"></span>
    <div>
      <div class="brand__name">Birchway Swing Studio's</div>
      <div class="brand__tagline">New indoor location is open!</div>
    </div>
  </div>

  <div class="abs offers">
    <h2 class="offers__title">Our training facility offers :</h2>
    <ul class="offers__list">
      <li>Award winner instruction</li>
      <li>State-of-the-art technology</li>
      <li>Custom club fitting</li>
    </ul>
  </div>

  <p class="abs intro">Whether you are a beginner, an aspiring athlete,<br>or an amateur, Birchway Swing Studio offers personalized<br>programs to help take your game to the next level.</p>

  <div class="abs golfer" role="img" aria-label="Silhouette of a golfer finishing a swing"></div>

  <div class="abs cta">
    <div class="cta__line1">CALL NOW TO SCHEDULE YOUR</div>
    <div class="cta__line2">FREE TOUR OR TO SIGN UP</div>
  </div>

  <div class="abs contact">
    <div class="contact__phone">555-014-2760</div>
    <div class="contact__email">hello@birchwayswing.com</div>
  </div>

  <p class="abs footnote">*Limited memberships available</p>

  <div class="abs rule" style="top:265px"></div>
  <div class="abs rule" style="top:306px"></div>
  <div class="abs rule" style="top:346px"></div>
  <div class="abs rule" style="top:387px"></div>
</section>

<section class="postcard postcard--front" aria-label="Postcard front">
  <svg class="abs front__photo" viewBox="0 0 740 572" role="img" aria-label="Close-up of a putting green with a golf ball beside the cup">
    <defs>
      <linearGradient id="grass" x1="0" y1="0" x2="0" y2="1">
        <stop offset="0" stop-color="#a4c13e"/>
        <stop offset=".55" stop-color="#7ea42a"/>
        <stop offset="1" stop-color="#3f6c14"/>
      </linearGradient>
      <radialGradient id="ball" cx="530" cy="453" r="82" gradientUnits="userSpaceOnUse">
        <stop offset="0" stop-color="#f2f4f5"/>
        <stop offset=".85" stop-color="#dfe5e8"/>
        <stop offset="1" stop-color="#dfe5e8" stop-opacity="0"/>
      </radialGradient>
    </defs>
    <rect width="740" height="572" fill="url(#grass)"/>
    <rect width="740" height="572" fill="url(#ball)"/>
  </svg>

  <svg class="abs front__band" viewBox="0 0 740 130" preserveAspectRatio="none" aria-hidden="true">
    <path d="M0 0 H740 V130 Q370 40 0 130 Z" fill="var(--red)"/>
  </svg>

  <h1 class="abs headline">Don't put away your clubs just yet!</h1>

  <svg class="abs front__map" viewBox="0 0 740 572" role="img" aria-label="Street map showing the studio location">
    <defs>
      <linearGradient id="mapTone" x1="0" y1="0" x2="1" y2="1">
        <stop offset="0" stop-color="#f1f1ef"/>
        <stop offset="1" stop-color="#e6e6e2"/>
      </linearGradient>
    </defs>
    <path d="M0 181 L303 113 L351 356 L268 372 L254 414 L238 378 L0 438 Z" fill="url(#mapTone)" stroke="#ffffff" stroke-width="5" stroke-linejoin="round"/>
  </svg>

  <div class="abs pitch__lead">The course may be closed but</div>
  <div class="abs pitch__name">Birchway Swing Studio's</div>
  <div class="abs pitch__tag">NEW INDOOR</div>
  <div class="abs pitch__rest">LOCATION IS</div>
  <div class="abs pitch__open">OPEN!</div>

  <address class="abs locator__card">4180 Larkfield Ave<br>Unit B3<br>Alderbrook, OH 45999</address>
  <span class="abs locator__dot"></span>
</section>

</body>
</html>
```